Flyer Template

I need a flyer template for door knocking on properties. Text Boxes need to be editable, with a header and text body. Footer to be my info. Project to be stylized to match my real estate signs and logo art from past projects

```html
<!DOCTYPE html>
<html lang="en">
<head>
<meta charset="utf-8">
<title>Marlow Realty – Door Knocking Flyer</title>
<link rel="stylesheet" href="https://fonts.googleapis.com/css2?family=Open+Sans:wght@400;700&family=Cinzel:wght@400;700&family=Roboto+Condensed:wght@300;400&display=swap">
<style>
  :root {
    --brand-red: #ee2a33;
    --ink-black: #050505;
    --logo-ink: #1c1c1c;
    --body-ink: #222222;
    --paper: #ffffff;
    --pattern-grey: #e9e9e9;
    --muted-grey: #6d6d6d;
    --partner-red: #b8262c;
  }
  * { box-sizing: border-box; margin: 0; padding: 0; }
  html, body { width: 1200px; height: 1200px; overflow: hidden; background: var(--paper); }
  .flyer {
    position: absolute; left: 179px; top: 301px;
    width: 842px; height: 598px;
    background: linear-gradient(100deg, var(--pattern-grey) 0%, #f6f6f6 35%, var(--paper) 60%);
    box-shadow: 0 1px 4px rgba(0,0,0,0.18);
    overflow: hidden;
    font-family: "Open Sans", sans-serif;
  }
  .flyer-shapes { position: absolute; inset: 0; width: 100%; height: 100%; }
  .brand-name {
    position: absolute; left: 55px; top: 126px; width: 200px;
    text-align: center; font-weight: 700; font-size: 30px; line-height: 38px;
    color: var(--logo-ink); letter-spacing: 0.5px;
  }
  .headline {
    position: absolute; left: 52px; top: 236px;
    color: var(--paper); font-size: 24.5px; line-height: 29px; letter-spacing: 0.3px;
  }
  .headline strong { font-weight: 700; }
  .body-copy {
    position: absolute; left: 56px; top: 355px; width: 492px;
    font-size: 13.4px; line-height: 17px; color: var(--body-ink);
  }
  .partner {
    position: absolute; left: 56px; top: 471px;
    font-family: "Roboto Condensed", sans-serif; color: var(--muted-grey);
  }
  .partner-name { font-size: 19px; line-height: 20px; letter-spacing: -0.5px; }
  .partner-name span { color: var(--partner-red); }
  .partner-sub { font-size: 7.5px; font-weight: 300; letter-spacing: 0.2px; }
  .contact {
    position: absolute; left: 38px; color: var(--paper);
    font-family: "Cinzel", serif; display: flex; align-items: center; gap: 16px;
  }
  .contact-phone { top: 525px; font-size: 27px; font-weight: 700; }
  .contact-email { top: 560px; font-size: 22px; }
  .contact svg { width: 30px; height: 28px; flex: none; }
  .agent-name {
    position: absolute; left: 548px; top: 540px; width: 262px;
    text-align: center; font-family: "Cinzel", serif; font-weight: 700;
    font-size: 25px; color: var(--paper); letter-spacing: 0.5px;
  }
</style>
</head>
<body>
<main class="flyer">
  <svg class="flyer-shapes" viewBox="0 0 1356 962" preserveAspectRatio="none" aria-hidden="false">
    <defs>
      <linearGradient id="lodge-tone" x1="0" y1="0" x2="0" y2="1">
        <stop offset="0" stop-color="#5a6a94"/>
        <stop offset="0.45" stop-color="#6b5a58"/>
        <stop offset="1" stop-color="#5b3a2a"/>
      </linearGradient>
      <linearGradient id="house-tone" x1="0" y1="0" x2="0" y2="1">
        <stop offset="0" stop-color="#9cc1e6"/>
        <stop offset="0.5" stop-color="#6f8a55"/>
        <stop offset="1" stop-color="#3d5a2e"/>
      </linearGradient>
      <radialGradient id="portrait-tone" cx="0.5" cy="0.5" r="0.6">
        <stop offset="0" stop-color="#c5412b"/>
        <stop offset="1" stop-color="#8a1d16"/>
      </radialGradient>
    </defs>
    <polygon role="img" aria-label="Photo of a log and stone luxury home at dusk"
             fill="url(#lodge-tone)"
             points="590,0 1356,0 1356,310 1170,505 930,600 450,155"/>
    <polygon points="1356,342 1292,405 1356,462" fill="var(--brand-red)"/>
    <polygon role="img" aria-label="Photo of a white house with trees and a black fence"
             fill="url(#house-tone)"
             points="1180,508 1270,418 1356,482 1356,824 905,824"/>
    <polygon points="0,351 645,351 873,558 0,558" fill="var(--brand-red)"/>
    <polygon points="0,824 880,824 760,958 0,958" fill="var(--ink-black)"/>
    <polygon points="898,824 1356,824 1356,962 780,962" fill="var(--brand-red)"/>
    <polygon points="260,958 760,958 757,962 255,962" fill="var(--brand-red)"/>
    <circle cx="1090" cy="664" r="170" fill="var(--paper)"/>
    <circle role="img" aria-label="Portrait photo of the agent" cx="1090" cy="664" r="160" fill="url(#portrait-tone)"/>
  </svg>

  <div class="brand-name">MARLOW<br>REALTY</div>

  <h1 class="headline"><strong>WE BELIEVE CREATING</strong><br>A BETTER WORLD STARTS WITH<br>HELPING OUR NEIGHBORS.</h1>

  <p class="body-copy">Lorem ipsum dolor sit amet, consectetur adipiscing elit, sed do eiusmod tempor incididunt ut labore et dolore magna aliqua. Quis ipsum suspendisse ultrices gravida. Risus commodo viverra maecenas accumsan lacus vel facilisis.</p>

  <div class="partner">
    <div class="partner-name">NORTHLINE GROUP</div>
    <div class="partner-sub">NORTHLINE PARTNERS REALTY</div>
  </div>

  <div class="contact contact-phone">
    <svg viewBox="0 0 30 28" aria-hidden="true"><path d="M7 3 L11 8 L9 11 Q11 16 16 19 L19 17 L24 21 L21 25 Q10 24 4 9 Z" fill="none" stroke="#fff" stroke-width="2" stroke-linejoin="round"/><path d="M17 4 Q24 5 25 12 M17 8 Q21 9 21 12" fill="none" stroke="#fff" stroke-width="1.6"/></svg>
    <span>555-014-2270</span>
  </div>
  <div class="contact contact-email">
    <svg viewBox="0 0 30 28" aria-hidden="true"><rect x="2" y="5" width="26" height="19" fill="none" stroke="#fff" stroke-width="2"/><path d="M2 5 L15 16 L28 5 M2 24 L12 14 M28 24 L18 14" fill="none" stroke="#fff" stroke-width="2"/></svg>
    <span>JMARLOW@EXAMPLE.COM</span>
  </div>

  <div class="agent-name">JORDAN MARLOW</div>
</main>
</body>
</html>
```